Nutrition Consulting Business needs a Postcard

I am a nutritionist and I need a brochure that highlights my consulting company called, GreenLeaf OakPath. Nutrition counselling helps the individual understand why we make certain health choices and help achieve meaningful resolutions to these difficult roadblocks. It is the practice of incorporating diverse nutritional and health philosophies to identify and achieve goals that lead to improved health and well-being. Nutrition counselling facilitates personal ownership in ones life choices, and provides the individual with the knowledge and the resources to make decisions that will be vital to their health and well-being. The important caveat of nutrition counselling is to gradually modify ones choices to ensure that changes last the their whole life. I want something that is professional, clean and makes people want to kickstart their wellness journey.
www.greenleafoakpath.example
Updates

I have updated the project profile (more detail) and changed to a guaranteed funds project. happy designing!

Target Market(s)

open minded adults and families wanting to make changes to better their health, those with gastrointestinal problems

Industry/Entity Type

Nutrition

Requirements
Must have
• The brochure must have my logo but I am open to font etc. I would liek to stick with 'earthy' colours, focusing on greens, like in my logo with eggplant as an accent colour.

Email: marla@greenleafoakpath.example
FB: https://www.facebook.com/greenleafoakpath
T: @greenleafoakpath

I am not sure what would be the best way to display this information. Maybe you have some ideas?

I would like to have my name and credentials stated somewhere. It is my PhD that sets be apart from others in the industry.
Marla Quenby
PhD Clinical Nutrition
Certified Health Coach

My main tag line is: "Leaf green, path oak." Maybe that could be the focus on the front side. With the 'big changes' quote on the backside somewhere.

Also, I think it would be valuable to have a brief list of services (what I do):
Individual Consultations
Workshops
Corporate Seminars
Meal Planning
Fresh Start Reset

Feel free to use any content from my website.
Nice to have
• I would prefer a two sided card type brochure. It would be nice if the design could easily fit to a 4X6 index/recipe card format also.

```html
<!DOCTYPE html>
<html lang="en">
<head>
<meta charset="utf-8">
<title>Recipe Card – Strawberry Cake Pops</title>
<link rel="stylesheet" href="https://fonts.googleapis.com/css2?family=Source+Sans+3:ital,wght@0,400;0,600;0,700;1,400;1,600&display=swap">
<style>
  :root{
    --leaf:#a8c96b;
    --eggplant:#8a5b8d;
    --ink:#262626;
    --white:#ffffff;
    --quote-mark:rgba(255,255,255,.55);
    --band-dark:#1f2430;
    --band-mid:#3a3f55;
    --band-warm:#6b4031;
    --photo-top:#4a3a35;
    --photo-bottom:#33261f;
  }
  *{margin:0;padding:0;box-sizing:border-box}
  html,body{width:800px;height:1200px;overflow:hidden;background:var(--leaf)}
  .card{
    position:relative;width:800px;height:1200px;background:var(--leaf);
    font-family:"Source Sans 3","Myriad Pro",Arial,sans-serif;color:var(--ink);
  }
  h1,h2,h3{font-size:inherit;line-height:inherit}
  /* Quote */
  .quote{position:absolute;left:0;top:0;width:800px;height:200px}
  .quote-mark{
    position:absolute;font-family:Georgia,"Times New Roman",serif;font-weight:700;
    color:var(--quote-mark);font-size:120px;line-height:1;
  }
  .quote-mark.open{left:92px;top:14px}
  .quote-mark.close{left:562px;top:112px}
  .quote-line{position:absolute;white-space:nowrap}
  .quote-strong{color:var(--eggplant);font-weight:700;letter-spacing:.5px}
  .quote-soft{color:var(--white);font-style:italic;font-weight:400}
  .line-1{left:163px;top:38px;font-size:43px}
  .line-1 .quote-soft{font-size:28px}
  .line-2{left:170px;top:86px;font-size:28px}
  .line-3{left:242px;top:122px;font-size:49px}
  /* Title band */
  .title-band{
    position:absolute;left:0;top:200px;width:800px;height:48px;
    background:linear-gradient(90deg,var(--band-dark) 0%,var(--band-mid) 30%,var(--band-warm) 45%,var(--band-mid) 60%,var(--band-dark) 100%);
  }
  .title-band h1{
    position:absolute;left:39px;top:10px;font-size:21px;font-weight:700;color:var(--white);
  }
  /* Columns */
  .column{position:absolute;font-size:17.6px;line-height:22.2px}
  .column-left{left:42px;top:259px;width:360px}
  .column-right{left:418px;top:259px;width:372px}
  .section-title{font-weight:700}
  .sub-title{font-weight:700;padding-left:16px}
  .ingredient-list{list-style:none;padding-left:33px}
  .directions{margin-top:26px}
  .steps{list-style:none}
  .step{display:grid}
  .column-left .step{grid-template-columns:20px 1fr}
  .column-right .step{grid-template-columns:29px 1fr}
  /* Photo */
  .photo{
    position:absolute;left:418px;top:964px;width:382px;height:236px;border-radius:4px 0 0 0;
    background:linear-gradient(180deg,var(--photo-top),var(--photo-bottom));
  }
</style>
</head>
<body>
<main class="card">
  <header class="quote">
    <span class="quote-mark open">“</span>
    <p class="quote-line line-1"><span class="quote-strong">BIG COMMITMENTS</span> <span class="quote-soft">to small</span></p>
    <p class="quote-line line-2"><span class="quote-soft">changes outlast small commitments to</span></p>
    <p class="quote-line line-3"><span class="quote-strong">BIG CHANGES</span></p>
    <span class="quote-mark close">”</span>
  </header>

  <div class="title-band" role="img" aria-label="Strip photo of blueberries and a wooden spoon">
    <h1>Recipe / Strawberry Cake Pops</h1>
  </div>

  <section class="column column-left">
    <h2 class="section-title">Ingredients</h2>
    <h3 class="sub-title">Cake:</h3>
    <ul class="ingredient-list">
      <li>cup cane sugar</li>
      <li>1/2 all purpose gluten free flour mix,<br>sifted</li>
      <li>1 tsp xanthan gum</li>
      <li>1/2 tsp salt</li>
      <li>1 tsp baking powder</li>
      <li>3/4 cup coconut oil, melted</li>
      <li>1/2 cup non-dairy milk</li>
      <li>1 tbsp apple cider vinegar</li>
      <li>8 large strawberries</li>
    </ul>
    <h3 class="sub-title">Cake Pop Coating:</h3>
    <ul class="ingredient-list">
      <li>3 cups dark chocolate</li>
      <li>1/4 coconut oil</li>
    </ul>
    <h3 class="sub-title">Other Supplies:</h3>
    <ul class="ingredient-list">
      <li>25 lollipop sticks</li>
      <li>coconut, shredded unsweetened<br>chocolate chips</li>
    </ul>

    <div class="directions">
      <h2 class="section-title">Directions</h2>
      <ol class="steps">
        <li class="step"><span>1.</span><span>Preheat oven to 350 degrees and<br>prepare cake pan by greasing with<br>coconut oil and lightly flouring.</span></li>
        <li class="step"><span>2.</span><span>Mix together sugar, gluten free flour,<br>xanthan gum, baking powder and salt<br>until well blended.</span></li>
        <li class="step"><span>3.</span><span>Combine non-dairy milk and melted<br>Green Churn and slowly stir into flour<br>mix until a thick batter is formed. Add<br>vinegar slowly, stirring in between.</span></li>
        <li class="step"><span>4.</span><span>Pour batter into prepared cake pan.<br>Bake at 350 degrees for about<br>40 minutes, or until knife inserted<br>into center comes out clean. Let cool<br>completely.</span></li>
        <li class="step"><span>5.</span><span>Puree the fresh strawberries and set<br>aside.</span></li>
        <li class="step"><span>6.</span><span>After cake is cooked and cooled<br>completely, crumble into large bowl.</span></li>
      </ol>
    </div>
  </section>

  <section class="column column-right">
    <ol class="steps">
      <li class="step"><span>7.</span><span>Mix thoroughly with pureed<br>strawberries. Add small amounts of<br>pureed strawberries at a time. Use<br>your hands and mix until sticky but<br>not too moist.</span></li>
      <li class="step"><span>8.</span><span>Roll mixture into quarter size balls and<br>place on wax paper covered cookie<br>sheet. (Should make 25-30).</span></li>
      <li class="step"><span>9.</span><span>Place them in the freezer for a<br>15 minutes to firm up.</span></li>
      <li class="step"><span>10.</span><span>Melt chocolate and coconut oil in<br>a double boiler or on the stove top<br>on low heat. Do not over heat. The<br>chocolate mixture should be room<br>temperature when it is all melted.</span></li>
      <li class="step"><span>11.</span><span>Once the cake balls are firm, dip<br>the tip of your lollipop stick in the<br>chocolate coating and insert into the<br>cake balls (about half way).</span></li>
      <li class="step"><span>12.</span><span>Carefully insert the cake ball into the<br>candy coating by holding the lollipop<br>stick and rotating until covered. Once<br>covered remove and softly tap and<br>rotate until the excess chocolate falls<br>off. Don’t tap too hard or the cake ball<br>will fall off, too.</span></li>
      <li class="step"><span>13.</span><span>Sprinkled cake pop with shredded<br>coconut or chocolate chips to finish<br>them off.</span></li>
      <li class="step"><span>14.</span><span>Place in a styrofoam block or in tall<br>glass cups to dry.</span></li>
    </ol>
  </section>

  <div class="photo" role="img" aria-label="Photo of chocolate-dipped strawberry cake pops, one rolled in shredded coconut and one cut open"></div>
</main>
</body>
</html>
```